Mobile Recording Studio needs business cards

Open to seeing a creative design, but I want to emphasis my logo and minimize the name/title and company information. Possible a fully black background on card.

My company is a mobile sound recording studio. ok to include a my trailer (actual or cartoon) on the card. My initial thought is more straight forward, but a good design will win me over.

SPECS:
CMYK color mode
High (300ppi) raster effect.
cover bleed area
please deliver: Illustrator file with layers and a pdf at completion.

Name and info for the business card:

Dallin Perry
ADR Mixer

email: Dallin@MixVault.com

address:
248 - 5170 East Hollister
Vancouver, BC V5R 2J4

phone:
604.518.2093 office

website:
www.MixVault.com

FB: @MixVault

Instagram: @TheMixVault

Industry/Entity Type

Television Production

Contact Information for Business Card

Dallin Perry
ADR Mixer

email: Dallin@MixVault.com

address:
248 - 5170 East Hollister
Vancouver, BC V5R 2J4

phone:
604.518.2093 office

website:
www.MixVault.com

FB: @MixVault

Instagram: @TheMixVault

Colors

Designer to choose colors to be used in the design.

Requirements
Must have
• emphasis my logo and minimize the name/title and company information.
• SPECS:
• CMYK color mode
• High (300ppi) raster effect.
• cover bleed area
• please deliver: Illustrator file with layers and a pdf at completion.
Nice to have
• maybe include the following:
• all black background or black theme
• my work trailer (actual or cartoon) refer to Instagram: @TheMixVault

```html
<!DOCTYPE html>
<html lang="en">
<head>
<meta charset="utf-8">
<title>MixVault Business Cards</title>
<link rel="stylesheet" href="https://fonts.googleapis.com/css2?family=Montserrat:wght@400;500;700&display=swap">
<style>
  :root {
    --backdrop: #3a332e;
    --card-black: #2a2a2c;
    --logo-gloss: #141415;
    --card-white: #ffffff;
    --ink: #111111;
    --rule: #1c1c1c;
  }
  * { margin: 0; padding: 0; box-sizing: border-box; }
  html, body {
    width: 1200px;
    height: 800px;
    overflow: hidden;
    background: var(--backdrop);
    font-family: "Montserrat", sans-serif;
  }
  .canvas {
    position: relative;
    width: 1200px;
    height: 800px;
  }
  .card {
    position: absolute;
    top: 252px;
    width: 525px;
    height: 300px;
    box-shadow: 0 10px 30px rgba(0,0,0,0.45);
  }
  .card--front {
    left: 50px;
    background: var(--card-black);
    display: flex;
    align-items: center;
    justify-content: center;
  }
  .card--back {
    left: 625px;
    background: var(--card-white);
    display: flex;
    align-items: center;
    padding-left: 44px;
  }
  .brand-name {
    font-family: "Montserrat", sans-serif;
    font-weight: 700;
    letter-spacing: 1px;
  }
  .card--front .brand-name {
    font-size: 62px;
    color: var(--logo-gloss);
  }
  .card--back .brand-name {
    font-size: 38px;
    color: var(--ink);
    width: 200px;
  }
  .divider {
    width: 1px;
    height: 170px;
    background: var(--rule);
    margin: 0 16px 0 14px;
  }
  .contact {
    color: var(--ink);
    font-size: 12.5px;
    line-height: 1.32;
  }
  .contact__name {
    font-weight: 700;
    font-size: 15px;
    letter-spacing: 0.5px;
    text-transform: uppercase;
  }
  .contact__title { margin-bottom: 4px; }
  .contact__address { margin-bottom: 4px; }
  .contact__row {
    display: flex;
    align-items: center;
    gap: 6px;
  }
  .contact__icon {
    width: 11px;
    height: 11px;
    flex: none;
  }
</style>
</head>
<body>
<main class="canvas">
  <section class="card card--front" aria-label="Card front">
    <span class="brand-name">MixVault</span>
  </section>

  <section class="card card--back" aria-label="Card back">
    <span class="brand-name">MixVault</span>
    <span class="divider"></span>
    <div class="contact">
      <div class="contact__name">Dallin Perry</div>
      <div class="contact__title">ADR Mixer</div>
      <div class="contact__address">248 - 5170 East Hollister<br>Vancouver, BC V5R 2J4</div>
      <div class="contact__row">
        <svg class="contact__icon" viewBox="0 0 12 12" aria-hidden="true"><path d="M2.5 1 L4.5 1 L5.3 3.4 L4 4.4 Q5 6.8 7.6 8 L8.6 6.7 L11 7.5 L11 9.5 Q10.6 11 9 11 Q1 10 1 3 Q1 1.4 2.5 1 Z" fill="var(--ink)"/></svg>
        <span>604.518.2093</span>
      </div>
      <div class="contact__row">
        <svg class="contact__icon" viewBox="0 0 12 12" aria-hidden="true"><rect x="0.5" y="2" width="11" height="8" fill="var(--ink)"/><path d="M0.8 2.4 L6 6.6 L11.2 2.4" stroke="#fff" stroke-width="1" fill="none"/></svg>
        <span>Dallin@MixVault.com</span>
      </div>
      <div class="contact__row">
        <svg class="contact__icon" viewBox="0 0 12 12" aria-hidden="true"><circle cx="6" cy="6" r="5.5" fill="var(--ink)"/></svg>
        <span>www.MixVault.com</span>
      </div>
      <div class="contact__row">
        <svg class="contact__icon" viewBox="0 0 12 12" aria-hidden="true"><rect x="0.5" y="0.5" width="11" height="11" rx="2" fill="var(--ink)"/></svg>
        <span>@MixVault</span>
      </div>
      <div class="contact__row">
        <svg class="contact__icon" viewBox="0 0 12 12" aria-hidden="true"><rect x="0.5" y="0.5" width="11" height="11" rx="2" fill="var(--ink)"/></svg>
        <span>@TheMixVault</span>
      </div>
    </div>
  </section>
</main>
</body>
</html>
```